Tallwater Builders Guild Membership

UPDATED files - 06/03/2021
Digital brochure needed for construction contractor related nonprofit organization.
Document will be primarily for digital viewing with potential for print version. Should be branded with our branding (logo attached). This is intended to be a multiple page document, plan to print and web (email) use. Standard Letter size document 8.5 x 11 inch
Portrait format preferred
The attached project brief includes a cover, 4 internal pages, and a back cover. This is flexible pending design layout
Target Market(s)
Residential construction business owners
Requirements
Must have
- See attached brief.Orange color palette: RGB: (253,153,0)
Nice to have
- See attached bief
Should not have
- No suit or ties. button up shirt okay, but not white collar worker.

```html
<!DOCTYPE html>
<html lang="en">
<head>
<meta charset="utf-8">
<title>Tallwater Builders Guild – Membership Brochure</title>
<link rel="stylesheet" href="https://fonts.googleapis.com/css2?family=Montserrat:wght@400;500;600;700;800;900&family=Oswald:wght@400;500&display=swap">
<style>
  :root{
    --orange:#fd9900;
    --dark:#3a3a3a;
    --ink:#222222;
    --grey:#ebebeb;
    --mid:#9a9a9a;
    --stage:#c9c9c9;
    --white:#ffffff;
  }
  *{box-sizing:border-box;margin:0;padding:0}
  html,body{width:1200px;height:2895px;overflow:hidden}
  body{
    background:var(--stage);
    font-family:'Montserrat',sans-serif;
    color:var(--ink);
    display:flex;flex-direction:column;justify-content:space-evenly;
    padding:0 40px;
  }
  .spread{display:flex;justify-content:space-between}
  .page{
    position:relative;width:540px;height:699px;background:var(--white);
    box-shadow:0 3px 10px rgba(0,0,0,.28);overflow:hidden;
  }

  /* brand name */
  .brand{text-align:center;color:var(--ink);font-weight:900;line-height:1}
  .brand-name{display:block;letter-spacing:-.5px}
  .brand-sub{display:block;letter-spacing:9px;margin-top:3px}
  .brand--inline .brand-name{font-size:23px}
  .brand--inline .brand-sub{font-size:9px;letter-spacing:8px}
  .brand--stacked .brand-name{font-size:38px;line-height:1.02}
  .brand--stacked .brand-sub{font-size:14px;letter-spacing:12px;margin-top:6px}

  .masthead{
    height:154px;display:flex;align-items:center;justify-content:center;
    background:linear-gradient(180deg,#ffffff 0%,#e2e2e2 100%);
  }

  /* footer strip */
  .page-foot{
    position:absolute;left:0;right:0;bottom:22px;height:19px;background:var(--orange);
    color:var(--white);font-size:9.5px;letter-spacing:3.2px;font-weight:500;
    display:flex;align-items:center;padding:0 22px;
  }
  .page-num{
    position:absolute;right:14px;top:-2px;width:23px;height:23px;border-radius:50%;
    background:var(--dark);border:2px solid var(--white);color:var(--white);
    font-size:10px;font-weight:700;letter-spacing:0;display:flex;align-items:center;justify-content:center;
  }

  /* cover */
  .cover-photo{
    position:absolute;top:154px;left:0;width:540px;height:368px;
    background:linear-gradient(120deg,#6b6f72 0%,#c58a2b 38%,#f2a52a 55%,#8a8d8c 78%,#d9d6c8 100%);
  }
  .cover-band{
    position:absolute;top:522px;left:0;right:0;height:128px;background:var(--dark);
    border-top:4px solid #d8d8d8;
    display:flex;flex-direction:column;align-items:center;justify-content:center;
    text-align:center;color:var(--white);font-weight:900;font-size:22px;line-height:1.36;letter-spacing:.8px;
  }
  .cover-band .accent{color:var(--orange)}
  .cover .page-foot{bottom:21px;justify-content:center}
  .cover-base{position:absolute;left:0;right:0;bottom:0;height:21px;background:var(--dark)}

  /* inner pages */
  .inner{padding:28px 32px 0}
  .inner .brand{margin-bottom:14px}
  .section-head{
    display:flex;align-items:center;gap:8px;height:24px;padding:0 8px;margin:10px 0 4px;
    background:linear-gradient(90deg,#e3e3e3 0%,#ffffff 85%);
    color:var(--orange);font-weight:900;font-size:18px;letter-spacing:.6px;text-transform:uppercase;
  }
  .section-head svg{width:17px;height:17px;flex:none}
  .section-head--dark{background:linear-gradient(90deg,#3a3a3a 0%,#6a6a6a 60%,#ffffff 100%)}
  .section-head--orange{background:linear-gradient(90deg,#fd9900 0%,#fdb64a 55%,#ffffff 100%);color:var(--white)}
  .copy{font-size:9.8px;line-height:1.3;text-align:justify;color:var(--ink)}
  .copy + .copy{margin-top:9px}
  .bullets{list-style:none;font-size:9.8px;font-weight:700;line-height:1.35}
  .bullets li::before{content:"• "}
  .bullets--orange li::before{color:var(--orange)}
  .sub-title{font-size:11px;font-weight:700;margin:8px 0 1px}

  .skill-grid{display:grid;grid-template-columns:1fr 1fr;gap:12px;margin:12px 0}
  .skill-box{background:var(--grey);padding:9px 12px;list-style:none;font-size:9.4px;font-weight:600;line-height:1.5}
  .skill-box li::before{content:"• "}

  /* membership */
  .page-title{color:var(--orange);font-weight:900;font-size:36px;letter-spacing:.6px;margin:4px 0 10px}
  .level-list{list-style:none;font-family:'Oswald',sans-serif;font-size:11.6px;line-height:1.8;color:var(--ink)}
  .level-list li{display:flex;align-items:center;gap:9px}
  .level-list svg{width:11px;height:11px;flex:none}
  .class-photo{
    margin:16px auto 0;width:442px;height:202px;
    background:linear-gradient(135deg,#4a4743 0%,#8c8478 35%,#d7d1c6 60%,#6f6a63 100%);
  }

  /* back cover */
  .directors{position:absolute;top:154px;left:0;right:0;height:420px;background:var(--orange);padding:22px 26px 0}
  .directors-title{color:var(--white);text-align:center;font-weight:900;font-size:33px;letter-spacing:1.2px;margin-bottom:20px}
  .director-grid{display:grid;grid-template-columns:1fr 1fr;row-gap:18px;column-gap:16px}
  .director{display:flex;gap:12px;align-items:flex-start}
  .portrait{
    width:108px;height:108px;border-radius:50%;flex:none;border:4px solid #f3f3f3;
    background:radial-gradient(circle at 50% 40%,#d9d9d9 0%,#a8a8a8 100%);
  }
  .director-text{font-family:'Oswald',sans-serif;color:var(--white);padding-top:4px}
  .director-name{font-size:14px;font-weight:500;line-height:1.3}
  .director-role{font-size:13px;line-height:1.3;margin-bottom:6px}
  .director-bio{font-size:9.6px;line-height:1.38}
  .contact{
    position:absolute;top:574px;left:0;right:0;height:84px;background:var(--dark);
    border-top:4px solid #d8d8d8;color:var(--white);text-align:center;
    font-size:13px;line-height:1.4;padding-top:6px;
  }
  .contact strong{font-weight:700}
  .back .page-foot{bottom:21px;justify-content:center}
</style>
</head>
<body>

<!-- row 1 -->
<div class="spread">
  <section class="page cover">
    <header class="masthead">
      <div class="brand brand--stacked"><span class="brand-name">TALLWATER<br>BUILDERS</span><span class="brand-sub">GUILD</span></div>
    </header>
    <div class="cover-photo" role="img" aria-label="Construction workers in hard hats and high-visibility vests reviewing plans on a job site"></div>
    <div class="cover-band">
      <div>HELPING YOU REDUCE RISKS AND</div>
      <div>INJURIES WHILE IMPROVING</div>
      <div class="accent">PROFITABILITY</div>
    </div>
    <footer class="page-foot">www.tallwaterguild.org</footer>
    <div class="cover-base"></div>
  </section>

  <section class="page inner">
    <div class="brand brand--inline"><span class="brand-name">TALLWATER BUILDERS</span><span class="brand-sub">GUILD</span></div>

    <h2 class="section-head"><svg viewBox="0 0 20 20"><circle cx="10" cy="10" r="8" fill="none" stroke="#3a3a3a" stroke-width="2"/><circle cx="10" cy="10" r="3.5" fill="none" stroke="#3a3a3a" stroke-width="2"/><path d="M10 10 L18 2" stroke="#3a3a3a" stroke-width="2"/></svg>Mission</h2>
    <p class="copy">To promote, educate and advance a diverse contractor community by providing pathways of accessibility to help build a stronger foundation for a better future.</p>

    <h2 class="section-head"><svg viewBox="0 0 20 20"><path d="M1 10 Q10 2 19 10 Q10 18 1 10Z" fill="none" stroke="#3a3a3a" stroke-width="2"/><circle cx="10" cy="10" r="3" fill="#3a3a3a"/></svg>Vision</h2>
    <p class="copy">To become the preferred organization for construction contractors striving to be the best in their trade through education, training, and ongoing development.</p>

    <h2 class="section-head section-head--dark"><svg viewBox="0 0 20 20"><circle cx="10" cy="10" r="6" fill="none" stroke="#ffffff" stroke-width="2" stroke-dasharray="3 2"/><circle cx="10" cy="10" r="2.5" fill="#ffffff"/></svg>Core Values</h2>
    <ul class="bullets">
      <li>Empower through learning &amp; development</li>
      <li>Strengthen &amp; sustain the industry</li>
      <li>Build partnerships to benefit underserved communities</li>
      <li>Act with integrity, respect, and honesty</li>
      <li>Promote diversity, equity, and inclusion throughout the industry</li>
    </ul>

    <h2 class="section-head"><svg viewBox="0 0 20 20"><circle cx="10" cy="5" r="3" fill="#3a3a3a"/><circle cx="4" cy="8" r="2.3" fill="#3a3a3a"/><circle cx="16" cy="8" r="2.3" fill="#3a3a3a"/><rect x="6" y="10" width="8" height="8" rx="2" fill="#3a3a3a"/></svg>Diversity, Equity &amp; Inclusion</h2>
    <p class="copy">TBG promotes and encourages open dialogue and positive working environments for BIPOC and other identity groups, to thrive within a contractor community and facilitate a more inclusive and resilient future.</p>

    <h2 class="section-head section-head--orange"><svg viewBox="0 0 20 20"><circle cx="6" cy="7" r="3" fill="#ffffff"/><circle cx="14" cy="7" r="3" fill="#ffffff"/><rect x="1" y="11" width="9" height="6" rx="2" fill="#ffffff"/><rect x="10" y="11" width="9" height="6" rx="2" fill="#ffffff"/></svg>About Us</h2>
    <p class="copy">TBG is organized as a 501c6 membership organization supported by a 501c3 charitable foundation. Our foundation allows us to provide access to training and education resources to an underserved community of contractors, supporting them in developing a sustainable and profitable business.</p>
    <p class="copy">We invite you to join a community of contractors who are better prepared to overcome challenges within the industry, empowering them to share ideas, lessons learned, proven practices, and insights with other industry leaders.</p>

    <footer class="page-foot">www.tallwaterguild.org<span class="page-num">01</span></footer>
  </section>
</div>

<!-- row 2 -->
<div class="spread">
  <section class="page inner">
    <div class="brand brand--inline"><span class="brand-name">TALLWATER BUILDERS</span><span class="brand-sub">GUILD</span></div>

    <h2 class="section-head"><svg viewBox="0 0 20 20"><path d="M3 17 L12 8" stroke="#3a3a3a" stroke-width="3"/><circle cx="14" cy="6" r="4" fill="none" stroke="#3a3a3a" stroke-width="2"/><path d="M3 3 L17 17" stroke="#3a3a3a" stroke-width="2"/></svg>Technical Assistance</h2>
    <p class="copy">One of our primary goals is to provide technical assistance to the contractor community based on individual level of competency. We understand that the needs of contractors vary greatly based on experience, training, past mentorship. Technical assistance takes many forms including business formation assistance, contractor licensing (OR, WA), insurance consulting, access to legal resources as well as assistance with government program funding (PPP Loans, business grants, scholarships), and various networking opportunities.<br>We also provide technical assistance in one-on-one setting as well as business workshops and ongoing assistance. Additionally, we offer assistance with COBID initial and renewal applications.</p>

    <h2 class="section-head" style="margin-top:30px"><svg viewBox="0 0 20 20"><path d="M10 1 L18 4 V10 Q18 16 10 19 Q2 16 2 10 V4Z" fill="#3a3a3a"/><path d="M6 10 L9 13 L14 7" stroke="#ffffff" stroke-width="2" fill="none"/></svg>Safety &amp; Compliance</h2>
    <h3 class="sub-title">SafeLog</h3>
    <p class="copy">SafeLog.com is a secure, web-based application that enables employers to create each state's first report of injury, track injuries, and view injury metrics in real-time. The software includes the ability automatically generate and download PDF versions of OSHA forms 301, 300, and 300A to print, share, or email. Works with all devices: computers, tablets, and smartphones. Once data is entered and intuitively updated on all other forms, SafeLog will automatically generate benchmark figures with no additional input by location and log.</p>
    <h3 class="sub-title">CrewSafe</h3>
    <p class="copy">Our partnership with CrewSafe gives you the tools you need to protect your workers, meet compliance requirements, and create a positive workspace environment for your employees and others you may work with. CrewSafe's staff of safety professionals, safety trainers, and administrative staff combined with innovative technology has helped thousands of contractors across the nation save money and improve efficiency. Included in the mobile app are the following:</p>
    <ul class="bullets bullets--orange" style="margin-top:8px">
      <li>Over 1,200 bilingual (Spanish/English) safety lessons with digital signoff rosters</li>
      <li>An online form builder to create job and equipment-specific inspection forms</li>
      <li>Mobile-accessible document storage repository</li>
      <li>Live monthly webinars addressing safety topics</li>
    </ul>

    <footer class="page-foot">www.tallwaterguild.org<span class="page-num">02</span></footer>
  </section>

  <section class="page inner">
    <div class="brand brand--inline"><span class="brand-name">TALLWATER BUILDERS</span><span class="brand-sub">GUILD</span></div>

    <h2 class="section-head"><svg viewBox="0 0 20 20"><path d="M1 8 L10 4 L19 8 L10 12Z" fill="#3a3a3a"/><path d="M5 10 V14 Q10 17 15 14 V10" fill="#3a3a3a"/></svg>Contractor Education</h2>
    <p class="copy">We provide education through live classes, training workshops, and via eLearning courses. We provide in-class training for EPA/RRP Certification, CPR/First Aid certification, Fall Protection certification, and the Oregon CCB 16-hour Pre-licensing training. We also offer a full suite of online construction education courses to help contractors learn at their own pace and convenience. Courses are mobile-friendly and available in English or Spanish. Our online course catalog includes</p>
    <div class="skill-grid">
      <ul class="skill-box"><li>OSHA 10 &amp; 30 training</li><li>Trade-specific skills</li><li>Safety courses</li><li>Administrative courses</li></ul>
      <ul class="skill-box"><li>HAZWOPER</li><li>Construction management</li><li>Environmental exposure</li><li>And much more...</li></ul>
    </div>
    <p class="copy">We also offer targeted training tracks in specific skillsets to promote business development necessary to operate an efficient business. Skillsets include:</p>
    <div class="skill-grid">
      <ul class="skill-box"><li>Business operations</li><li>Business Law &amp; Contracts</li><li>Understanding financials</li></ul>
      <ul class="skill-box"><li>Safety &amp; Compliance training</li><li>Marketing &amp; Networking</li><li>Business Management / HR</li></ul>
    </div>

    <h2 class="section-head" style="margin-top:18px"><svg viewBox="0 0 20 20"><rect x="3" y="5" width="14" height="13" fill="#3a3a3a"/><rect x="6" y="2" width="8" height="3" fill="#3a3a3a"/><rect x="6" y="8" width="3" height="3" fill="#ffffff"/><rect x="11" y="8" width="3" height="3" fill="#ffffff"/></svg>Directory for Contractors</h2>
    <p class="copy"><strong>BuildersListing.com</strong> is a FREE effortless way for contractors to connect with property owners to search for a contractor in their local area. As marketing has evolved, contractors need to adopt a variety of online tools and technologies to help gain more online visibility which will result in more business for you. The site gives instant access to residential and commercial contractors, an online bid request system, links to the contractor's social media pages and a review system all in one spot.</p>
    <p class="copy">Create your business profile and easily manage your unlimited FREE Bid requests, reviews, social media, photo gallery, video links just to name a few. Having a profile listing adds legitimacy to your business. A prime advantage of having your business listed is the SEO and relevant incoming "links to your business". Link building is an important building block of any SEO campaign.</p>

    <footer class="page-foot">www.tallwaterguild.org<span class="page-num">03</span></footer>
  </section>
</div>

<!-- row 3 -->
<div class="spread">
  <section class="page inner">
    <div class="brand brand--inline"><span class="brand-name">TALLWATER BUILDERS</span><span class="brand-sub">GUILD</span></div>
    <h1 class="page-title">MEMBERSHIP LEVELS</h1>
    <ul class="level-list">
      <li><svg viewBox="0 0 12 12"><circle cx="6" cy="6" r="6" fill="#fd9900"/><path d="M3 6 L5.2 8 L9 4" stroke="#fff" stroke-width="1.6" fill="none"/></svg>OSHA Respiratory Protection per 29 CFR 1910.134</li>
      <li><svg viewBox="0 0 12 12"><circle cx="6" cy="6" r="6" fill="#fd9900"/><path d="M3 6 L5.2 8 L9 4" stroke="#fff" stroke-width="1.6" fill="none"/></svg>OSHA Safety Courses for General Industry and Construction per 29 CFR 1910 &amp; 29 CFR 1926</li>
      <li><svg viewBox="0 0 12 12"><circle cx="6" cy="6" r="6" fill="#fd9900"/><path d="M3 6 L5.2 8 L9 4" stroke="#fff" stroke-width="1.6" fill="none"/></svg>Spanish Courses (Versions in Spanish)</li>
      <li><svg viewBox="0 0 12 12"><circle cx="6" cy="6" r="6" fill="#fd9900"/><path d="M3 6 L5.2 8 L9 4" stroke="#fff" stroke-width="1.6" fill="none"/></svg>Human Resource Training</li>
      <li><svg viewBox="0 0 12 12"><circle cx="6" cy="6" r="6" fill="#fd9900"/><path d="M3 6 L5.2 8 L9 4" stroke="#fff" stroke-width="1.6" fill="none"/></svg>OSHA HAZWOPER per 29 CFR 1910.120(e) and (p) &amp; 29 CFR 1926.65(e) and (p)</li>
      <li><svg viewBox="0 0 12 12"><circle cx="6" cy="6" r="6" fill="#fd9900"/><path d="M3 6 L5.2 8 L9 4" stroke="#fff" stroke-width="1.6" fill="none"/></svg>Laboratory Safety per 29 CFR - Various</li>
      <li><svg viewBox="0 0 12 12"><circle cx="6" cy="6" r="6" fill="#fd9900"/><path d="M3 6 L5.2 8 L9 4" stroke="#fff" stroke-width="1.6" fill="none"/></svg>OSHA Hazmat Emergency Responder per 29 CFR 1910.120(q) &amp; 1926.65(q)</li>
      <li><svg viewBox="0 0 12 12"><circle cx="6" cy="6" r="6" fill="#fd9900"/><path d="M3 6 L5.2 8 L9 4" stroke="#fff" stroke-width="1.6" fill="none"/></svg>OSHA Hazard Communication (HAZCOM) and GHS per 29 CFR 1910.1200</li>
      <li><svg viewBox="0 0 12 12"><circle cx="6" cy="6" r="6" fill="#fd9900"/><path d="M3 6 L5.2 8 L9 4" stroke="#fff" stroke-width="1.6" fill="none"/></svg>Custom Online Training</li>
      <li><svg viewBox="0 0 12 12"><circle cx="6" cy="6" r="6" fill="#fd9900"/><path d="M3 6 L5.2 8 L9 4" stroke="#fff" stroke-width="1.6" fill="none"/></svg>Chemical Specific Training for General Industry and Construction per OSHA, EPA and DOT</li>
    </ul>
    <div class="class-photo" role="img" aria-label="Contractors seated at desks taking notes during a training class"></div>
    <footer class="page-foot">www.tallwaterguild.org<span class="page-num">04</span></footer>
  </section>

  <section class="page back">
    <header class="masthead">
      <div class="brand brand--stacked"><span class="brand-name">TALLWATER<br>BUILDERS</span><span class="brand-sub">GUILD</span></div>
    </header>
    <div class="directors">
      <h2 class="directors-title">KEY DIRECTORS</h2>
      <div class="director-grid">
        <div class="director">
          <div class="portrait" role="img" aria-label="Director portrait placeholder"></div>
          <div class="director-text"><div class="director-name">Daniel Reyes</div><div class="director-role">Designation</div><div class="director-bio">Lorem Ipsum is simply dummy text of the printing and typesetting industry. Lorem Ipsum has been.</div></div>
        </div>
        <div class="director">
          <div class="portrait" role="img" aria-label="Director portrait placeholder"></div>
          <div class="director-text"><div class="director-name">Daniel Reyes</div><div class="director-role">Designation</div><div class="director-bio">Lorem Ipsum is simply dummy text of the printing and typesetting industry. Lorem Ipsum has been.</div></div>
        </div>
        <div class="director">
          <div class="portrait" role="img" aria-label="Director portrait placeholder"></div>
          <div class="director-text"><div class="director-name">Daniel Reyes</div><div class="director-role">Designation</div><div class="director-bio">Lorem Ipsum is simply dummy text of the printing and typesetting industry. Lorem Ipsum has been.</div></div>
        </div>
        <div class="director">
          <div class="portrait" role="img" aria-label="Director portrait placeholder"></div>
          <div class="director-text"><div class="director-name">Daniel Reyes</div><div class="director-role">Designation</div><div class="director-bio">Lorem Ipsum is simply dummy text of the printing and typesetting industry. Lorem Ipsum has been.</div></div>
        </div>
      </div>
    </div>
    <address class="contact" style="font-style:normal">
      <strong>Tallwater Builders Guild</strong><br>
      2400 Riverbend Ave., Suite #100<br>
      Millbrook, OR 97000<br>
      Office: (555) 014-2290 &nbsp;|&nbsp; Fax: 555.019.0881<br>
      support@tallwaterguild.org
    </address>
    <footer class="page-foot">www.tallwaterguild.org</footer>
    <div class="cover-base"></div>
  </section>
</div>

</body>
</html>
```